Business Card For Video Production Company

Please NOTE: I've added some info to the must haves that I should have included at the start. Thank you.

I need a business card design for my video production company based in Orlando called Halvard Lens Productions. Our work consists of web video marketing (web videos), training videos, sales videos, conference and seminar video production...basically a lot of corporate based work.

We work with successful small businesses, not-for-profits and some Summit 700 type groups. We bring a lot of knowledge, experience and attention to detail to every project.

I'd like something that communicates strength, confidence, integrity, as well as creative vision. I want to stay away from the standard icons of the media and film industry. I'd like to emphasize the colors of my logo, and also the colors of my website which has a white background. Simple is good.

Our budgets are moderate...generally $1500 to $5000.

www.halvardlens.tv

PS...We don't do weddings or recitals, or that type of production.
Updates

I want to thank all the designers for your updates. There's way too many to be able to give feedback on for all. I hope you understand that. But wow…there are so many great designs everyone has offered. I can't thank you enough…each and everyone. I hope to make my decision soon. I'm not accepting anymore designs from new designers. Dean-

Target Market(s)

Successful small businesses, marketing directors, corporate communication directors, training and human resources professionals. forward thinking not-for profits. Since my company is based in Central Florida, most of my work comes from this area too.

Industry/Entity Type

Marketing

Requirements
Must have
• website address, www.halvardlens.tv
phone number, 407-555-2937
email address, dean@halvardlens.tv

Title
Dean Halvard
Owner/Creative Director

I'd like to have a single line that goes across illustrating our services, maybe separated with bullet points:

Marketing Videos, Corporate Videos, Conference & Seminar Video Production
Should not have
• No film or video icons.
No need to pull language or copy from my website.

```html
<!DOCTYPE html>
<html lang="en">
<head>
<meta charset="utf-8">
<title>Halvard Lens Productions – Business Card</title>
<link rel="stylesheet" href="https://fonts.googleapis.com/css2?family=Nunito:wght@400;600;800&display=swap">
<style>
  :root {
    --stage: #ececec;
    --card: #ffffff;
    --card-edge: #d6d6d6;
    --brand-blue: #2090d8;
    --soft-blue: #b3def3;
    --ink: #58595b;
    --ink-dark: #3f4042;
  }
  * { box-sizing: border-box; margin: 0; padding: 0; }
  html, body {
    width: 1200px; height: 377px; overflow: hidden;
    background: var(--stage);
    font-family: "Nunito", sans-serif;
  }
  .sheet { position: relative; width: 1200px; height: 377px; }
  .card {
    position: absolute; top: 27px;
    width: 563px; height: 323px;
    background: var(--card);
    border: 1px solid var(--card-edge);
    overflow: hidden;
  }
  .card--front { left: 24px; }
  .card--back { left: 615px; }
  .card__shape { position: absolute; inset: 0; width: 100%; height: 100%; }
  .wordmark {
    position: absolute;
    display: flex; align-items: center; gap: 10px;
    color: var(--ink-dark);
    font-weight: 800; font-size: 25px; letter-spacing: -0.3px;
    white-space: nowrap;
  }
  .wordmark__square { width: 22px; height: 22px; background: var(--brand-blue); flex: none; }
  .card--front .wordmark { left: 29px; top: 40px; }
  .card--back .wordmark { left: 150px; top: 162px; font-size: 27px; }
  .person { position: absolute; left: 28px; top: 129px; }
  .person__name { color: var(--brand-blue); font-weight: 800; font-size: 17px; }
  .person__title { color: var(--ink); font-size: 14px; margin-top: 4px; }
  .contacts { position: absolute; left: 28px; top: 190px; list-style: none; }
  .contacts li {
    display: flex; align-items: center; gap: 6px;
    color: var(--ink-dark); font-size: 13.5px; height: 23px;
  }
  .contacts svg { width: 12px; height: 12px; flex: none; }
  .address { position: absolute; left: 28px; top: 285px; color: var(--ink-dark); font-size: 13.5px; }
  .services {
    position: absolute; left: 250px; top: 244px;
    color: var(--brand-blue); font-size: 15px; line-height: 25px;
  }
  .services__dot { color: #9a9a9a; margin-right: 3px; }
  .services__gap { display: inline-block; width: 10px; }
</style>
</head>
<body>
<main class="sheet">
  <section class="card card--front" aria-label="Card front">
    <svg class="card__shape" viewBox="0 0 563 323" aria-hidden="true">
      <polygon points="395,0 563,0 563,323 470,323" fill="var(--soft-blue)"/>
    </svg>
    <div class="wordmark"><span class="wordmark__square"></span>Halvard Lens Productions</div>
    <div class="person">
      <p class="person__name">Dean Halvard</p>
      <p class="person__title">Owner/Creative Director</p>
    </div>
    <ul class="contacts">
      <li>
        <svg viewBox="0 0 12 12" aria-hidden="true"><circle cx="6" cy="6" r="6" fill="var(--brand-blue)"/><path d="M4 3.2 L5 3 L5.6 4.6 L5 5.2 Q5.6 6.5 6.8 7 L7.4 6.4 L9 7 L8.8 8 Q6.5 8.6 4.6 6.6 Q3 4.8 4 3.2Z" fill="#fff"/></svg>
        407-555-2937
      </li>
      <li>
        <svg viewBox="0 0 12 12" aria-hidden="true"><circle cx="6" cy="6" r="6" fill="var(--brand-blue)"/><rect x="3" y="4" width="6" height="4.2" fill="#fff"/><path d="M3 4 L6 6.4 L9 4" stroke="var(--brand-blue)" stroke-width="0.8" fill="none"/></svg>
        dean@halvardlens.tv
      </li>
      <li>
        <svg viewBox="0 0 12 12" aria-hidden="true"><circle cx="6" cy="6" r="6" fill="var(--brand-blue)"/><circle cx="6" cy="6" r="3" fill="none" stroke="#fff" stroke-width="0.9"/><line x1="3" y1="6" x2="9" y2="6" stroke="#fff" stroke-width="0.8"/></svg>
        www.halvardlens.tv
      </li>
    </ul>
    <p class="address">Street Name, City Name, Zip Code-00000</p>
  </section>

  <section class="card card--back" aria-label="Card back">
    <svg class="card__shape" viewBox="0 0 563 323" aria-hidden="true">
      <polygon points="0,0 165,0 95,323 0,323" fill="var(--soft-blue)"/>
    </svg>
    <div class="wordmark"><span class="wordmark__square"></span>Halvard Lens Productions</div>
    <p class="services">
      <span class="services__dot">•</span>Marketing Videos<span class="services__gap"></span><span class="services__dot">•</span>Corporate Videos<br>
      <span class="services__dot">•</span>Conference &amp; Seminar Video Production
    </p>
  </section>
</main>
</body>
</html>
```